A private security company called "Ventrell Security Services Ltd"

Hello everybody,

We need a web page for a company based in NZ. It is mainly an informative website so it would be wonderful if the designer puts their absolute best into making it a website that I would really appreciate. The website needs to show professionalism and also needs to make our web surfers find the information they need in a click. the company's colour is black and silver, and if those two colours could be integrated into the website it would be absolutely lovely. Please do contact me for any information.

Sincerely,
Dorian Valcourt

```html
<!DOCTYPE html>
<html lang="en">
<head>
<meta charset="utf-8">
<title>Ventrell Security Services Ltd</title>
<link href="https://fonts.googleapis.com/css2?family=Questrial&family=Source+Sans+3:wght@400;600&display=swap" rel="stylesheet">
<style>
  :root {
    --ink: #1a1a1a;
    --white: #ffffff;
    --page-grey: #b5b6ba;
    --silver: #d6d6d6;
    --muted: #707070;
    --nav-dark: #151515;
    --nav-mid: #2a2a2a;
    --nav-active: #5a5a5a;
    --footer: #000000;
    --footer-text: #dcdcdc;
    --rule: #cfcfcf;
  }
  * { margin: 0; padding: 0; box-sizing: border-box; }
  html, body { width: 1200px; height: 985px; overflow: hidden; }
  body {
    position: relative;
    background: var(--page-grey);
    font-family: "Source Sans 3", "Source Sans Pro", sans-serif;
    color: var(--ink);
  }
  .site-header {
    position: absolute; left: 0; top: 0; width: 1200px; height: 160px;
    background: linear-gradient(#ffffff, #f4f4f4);
    box-shadow: 0 2px 4px rgba(0,0,0,.15);
  }
  .brand {
    position: absolute; left: 102px; top: 52px;
    font-family: "Questrial", sans-serif; color: var(--ink);
    font-variant: small-caps; line-height: 1;
  }
  .brand-name { display: block; font-size: 31px; letter-spacing: 1px; }
  .brand-sub { display: block; font-size: 13px; margin-top: 4px; letter-spacing: .3px; }
  .call {
    position: absolute; left: 786px; top: 40px;
  }
  .call svg { position: absolute; left: 0; top: 5px; }
  .call-label {
    position: absolute; left: 73px; top: 0; white-space: nowrap;
    font-family: "Questrial", sans-serif; font-variant: small-caps;
    font-size: 29px; letter-spacing: 1.5px; color: var(--ink);
  }
  .call-number {
    position: absolute; left: 68px; top: 31px; white-space: nowrap;
    font-size: 25px; color: #222;
  }
  .main-nav {
    position: absolute; left: 100px; top: 120px; width: 1002px; height: 40px;
    background: linear-gradient(var(--nav-mid), var(--nav-dark));
    border-radius: 5px 5px 0 0; display: flex; overflow: hidden;
  }
  .main-nav a {
    display: flex; align-items: center; justify-content: center;
    color: var(--white); text-decoration: none; font-size: 15px; letter-spacing: .4px;
    border-right: 1px solid #000; box-shadow: inset -1px 0 0 #3b3b3b;
  }
  .main-nav a:last-child { border-right: none; box-shadow: none; }
  .main-nav a.is-active { background: linear-gradient(#6a6a6a, #454545); }
  .content-shell {
    position: absolute; left: 100px; top: 160px; width: 1002px; height: 710px;
    background: #f2f2f2;
  }
  .hero-photo {
    position: absolute; left: 0; top: 0; width: 1002px; height: 380px;
    background: linear-gradient(90deg, #ffffff 0%, #f6f6f6 45%, #cdcbc8 62%, #8a7d72 75%, #2a2a2c 90%, #e9e9e9 100%);
  }
  .hero-fade {
    position: absolute; left: 0; top: 0; width: 1002px; height: 380px;
    background: linear-gradient(90deg, #fff 0%, rgba(255,255,255,.9) 40%, rgba(255,255,255,0) 58%);
  }
  .hero-title {
    position: absolute; left: 27px; top: 100px;
    font-family: "Questrial", sans-serif; font-variant: small-caps;
    font-size: 66px; letter-spacing: 2px; color: var(--ink);
  }
  .hero-tagline {
    position: absolute; left: 30px; top: 188px;
    font-size: 25px; color: var(--muted); letter-spacing: .5px;
  }
  .welcome-card {
    position: absolute; left: 117px; top: 506px; width: 969px; height: 378px;
    background: var(--white); border: 1px solid #e2e2e2;
    text-align: center;
  }
  .welcome-title {
    margin-top: 24px;
    font-family: "Questrial", sans-serif; font-variant: small-caps; font-weight: 400;
    font-size: 41px; letter-spacing: 2px; color: var(--ink);
  }
  .welcome-text {
    width: 900px; margin: 16px auto 0; font-size: 14px; line-height: 22px; color: #2a2a2a;
  }
  .welcome-text + .welcome-text { margin-top: 22px; }
  .divider {
    position: absolute; left: 10px; top: 267px; width: 941px; height: 1px; background: var(--rule);
  }
  .service {
    position: absolute; height: 56px; background: var(--silver);
    display: flex; align-items: center; text-align: left;
    font-size: 14px; line-height: 17px; color: var(--ink);
  }
  .service svg { flex: none; margin: 0 11px 0 10px; }
  .site-footer {
    position: absolute; left: 0; top: 870px; width: 1200px; height: 115px;
    background: var(--footer); color: var(--footer-text); font-size: 14px;
  }
  .footer-links {
    position: absolute; left: 0; top: 35px; width: 1200px; text-align: center; white-space: nowrap;
  }
  .footer-links span.sep { margin: 0 14px; }
  .copyright {
    position: absolute; left: 0; top: 67px; width: 1200px; text-align: center; font-size: 13px;
  }
</style>
</head>
<body>
  <header class="site-header">
    <div class="brand">
      <span class="brand-name">Ventrell</span>
      <span class="brand-sub">Security Services Ltd.</span>
    </div>
    <div class="call">
      <svg width="58" height="58" viewBox="0 0 58 58" aria-hidden="true">
        <path d="M6 4h8v52H8c-4 0-6-3-6-6V8c0-2 2-4 4-4z" fill="#222"/>
        <rect x="17" y="6" width="40" height="42" rx="5" fill="#222"/>
        <rect x="22" y="10" width="30" height="9" fill="#fff"/>
        <g fill="#fff">
          <rect x="23" y="23" width="6" height="5"/><rect x="32" y="23" width="6" height="5"/><rect x="41" y="23" width="6" height="5"/>
          <rect x="23" y="31" width="6" height="5"/><rect x="32" y="31" width="6" height="5"/><rect x="41" y="31" width="6" height="5"/>
          <rect x="23" y="39" width="6" height="5"/><rect x="32" y="39" width="6" height="5"/><rect x="41" y="39" width="6" height="5"/>
        </g>
      </svg>
      <span class="call-label">Call Us</span>
      <span class="call-number">+1 (555) 0142-38-760</span>
    </div>
    <nav class="main-nav">
      <a class="is-active" style="width:104px">HOME</a>
      <a style="width:147px">ABOUT US</a>
      <a style="width:140px">TRAINING</a>
      <a style="width:128px">SAFETY</a>
      <a style="width:184px">SUSTAINABILITY</a>
      <a style="width:159px">CONTACT US</a>
      <a style="width:140px">CAREERS</a>
    </nav>
  </header>

  <main class="content-shell">
    <div class="hero-photo" role="img" aria-label="Security officer in a white shirt holding a two-way radio at his belt"></div>
    <div class="hero-fade"></div>
    <h1 class="hero-title">Experts</h1>
    <p class="hero-tagline">IN YOUR INTERESTS PROTECTION</p>
  </main>

  <section class="welcome-card">
    <h2 class="welcome-title">Welcome to Ventrell</h2>
    <p class="welcome-text">Lorem Ipsum is simply Lorem Ipsum has been the industry's standard dummy text ever since the 1500s, when an unknown printer took a galley of type and scrambled it to make book. It has survived not only five centuries, but also the leap into electronic typesetting, remaining has been the industry's standard dummy text ever since the 1500s, when an unknown printer took a galley of type and scrambled it to make book. It has survived not only five centuries, but also the leap into electronic essentially unchanged.</p>
    <p class="welcome-text">It has survived not only five centuries, but also the leap into electronic typesetting, remaining has been the industry's standard dummy text ever since the 1500s, when an unknown printer took a galley remaining has been the industry's standard</p>
    <div class="divider"></div>

    <div class="service" style="left:16px;top:291px;width:133px">
      <svg width="22" height="20" viewBox="0 0 22 20" aria-hidden="true"><path d="M1 11l4-3 4 5L19 1l2 2L9 19z" fill="#111"/></svg>
      <span>PROPERTY<br>GUARDS</span>
    </div>
    <div class="service" style="left:168px;top:292px;width:170px;font-size:13px">
      <svg width="22" height="20" viewBox="0 0 22 20" aria-hidden="true"><path d="M1 11l4-3 4 5L19 1l2 2L9 19z" fill="#111"/></svg>
      <span>CORPORATE EVENTS<br>SECURITY</span>
    </div>
    <div class="service" style="left:358px;top:291px;width:259px">
      <svg width="22" height="20" viewBox="0 0 22 20" aria-hidden="true"><path d="M1 11l4-3 4 5L19 1l2 2L9 19z" fill="#111"/></svg>
      <span>PERSONAL BODYGUARD FOR HIGH<br>NET WORTH INDIVIDUALS</span>
    </div>
    <div class="service" style="left:636px;top:295px;width:145px;height:51px">
      <svg width="22" height="20" viewBox="0 0 22 20" aria-hidden="true"><path d="M1 11l4-3 4 5L19 1l2 2L9 19z" fill="#111"/></svg>
      <span>SECURITY<br>CONSULTANCY</span>
    </div>
    <div class="service" style="left:801px;top:295px;width:150px;height:52px">
      <svg width="22" height="20" viewBox="0 0 22 20" aria-hidden="true"><path d="M1 11l4-3 4 5L19 1l2 2L9 19z" fill="#111"/></svg>
      <span>PRIVATE<br>INVESTIGATION</span>
    </div>
  </section>

  <footer class="site-footer">
    <div class="footer-links">
      <span>Property guards</span><span class="sep">|</span><span>Corporate events security</span><span class="sep">|</span><span>Personal bodyguard for high net worth individuals</span><span class="sep">|</span><span>Security consultancy</span><span class="sep">|</span><span>Private investigation</span>
    </div>
    <p class="copyright">Copyright © 2014 Ventrell Security Services LTD.</p>
  </footer>
</body>
</html>
```